Banner for County Fair

Need a banner with our logo primarily, but some other color/background work. Also include city name West Point, NE. Tagline that could be used is Fiber Optic Fast! Also visit www.tollbarnetlink.com to get a feel for the company.

```html
<!DOCTYPE html>
<html lang="en">
<head>
<meta charset="utf-8">
<title>Northlink County Fair Banners</title>
<link rel="stylesheet" href="https://fonts.googleapis.com/css2?family=Roboto:ital,wght@0,400;0,700;0,900;1,700&display=swap">
<style>
  :root {
    --page: #f3f3f1;
    --panel-a: #e3e5e7;
    --panel-b: #e1dfdc;
    --brand-blue: #1f6fa6;
    --text-blue: #2b5d92;
    --accent-green: #4cbf96;
    --ink: #1b1b1b;
    --photo-a-light: #e9e6e2;
    --photo-a-dark: #c9b39c;
    --photo-b-light: #e8e2da;
  }
  * { margin: 0; padding: 0; box-sizing: border-box; }
  html, body { width: 1200px; height: 857px; overflow: hidden; background: var(--page); }
  body { position: relative; font-family: "Roboto", sans-serif; }

  .banner {
    position: absolute;
    left: 60px;
    width: 1080px;
    height: 340px;
    overflow: hidden;
    box-shadow: 0 4px 10px rgba(0,0,0,0.25);
  }
  .banner--mother { top: 60px; background: var(--panel-a); }
  .banner--family { top: 457px; background: var(--panel-b); }

  .brand {
    position: absolute;
    left: 18px;
    top: 24px;
    display: flex;
    align-items: center;
    gap: 10px;
    z-index: 2;
  }
  .brand__dot {
    width: 22px; height: 22px;
    border: 3px solid var(--brand-blue);
    border-radius: 50%;
  }
  .brand__name {
    font-weight: 900;
    font-size: 50px;
    letter-spacing: -1px;
    color: var(--brand-blue);
    line-height: 1;
  }
  .tagline {
    position: absolute;
    left: 42px;
    top: 84px;
    font-weight: 700;
    font-style: italic;
    font-size: 27px;
    color: var(--text-blue);
    letter-spacing: 0.3px;
    z-index: 2;
  }

  .offer {
    position: absolute;
    top: 110px;
    height: 175px;
    z-index: 2;
  }
  .banner--mother .offer { left: 160px; width: 420px; }
  .banner--family .offer { left: 40px; width: 430px; }
  .offer__shape { position: absolute; inset: 0; width: 100%; height: 100%; }
  .offer__list {
    position: absolute;
    left: 50px;
    top: 42px;
    list-style: none;
  }
  .offer__item {
    display: flex;
    align-items: center;
    gap: 12px;
    height: 46px;
    font-weight: 700;
    font-size: 25px;
    color: var(--ink);
    letter-spacing: 0.3px;
    white-space: nowrap;
  }
  .offer__icon { width: 30px; height: 30px; flex: none; }

  .location {
    position: absolute;
    left: 14px;
    bottom: 14px;
    display: flex;
    align-items: center;
    gap: 14px;
    font-size: 25px;
    color: var(--text-blue);
    z-index: 2;
  }
  .location__pin { width: 22px; height: 36px; }

  .photo { position: absolute; top: 0; right: 0; height: 100%; z-index: 1; }
  .photo--mother {
    width: 500px;
    background: linear-gradient(110deg, var(--photo-a-light) 0%, #e2d3c4 45%, var(--photo-a-dark) 100%);
  }
  .photo--family {
    width: 568px;
    background: linear-gradient(120deg, var(--photo-b-light) 0%, #c98a6e 45%, #3e5fa8 75%, #8fbf6a 100%);
  }
</style>
</head>
<body>

<section class="banner banner--mother">
  <div class="brand"><span class="brand__dot"></span><span class="brand__name">NORTHLINK</span></div>
  <p class="tagline">FIBER OPTIC FAST</p>

  <div class="offer">
    <svg class="offer__shape" viewBox="0 0 430 175" preserveAspectRatio="none" aria-hidden="true">
      <polygon points="10,28 408,2 388,152 28,152" fill="var(--accent-green)"/>
      <polygon points="48,2 420,26 410,126 36,162" fill="none" stroke="var(--ink)" stroke-width="4"/>
    </svg>
    <ul class="offer__list">
      <li class="offer__item">
        <svg class="offer__icon" viewBox="0 0 24 24" aria-hidden="true"><path fill="var(--ink)" d="M6.6 10.8a15.1 15.1 0 0 0 6.6 6.6l2.2-2.2a1 1 0 0 1 1-.25 11.4 11.4 0 0 0 3.6.57 1 1 0 0 1 1 1V20a1 1 0 0 1-1 1A17 17 0 0 1 3 4a1 1 0 0 1 1-1h3.5a1 1 0 0 1 1 1c0 1.25.2 2.45.57 3.57a1 1 0 0 1-.25 1z"/><path d="M14 3a7 7 0 0 1 7 7M14 6.5a3.5 3.5 0 0 1 3.5 3.5" fill="none" stroke="var(--ink)" stroke-width="1.8" stroke-linecap="round"/></svg>
        High Speed Internet
      </li>
      <li class="offer__item">
        <svg class="offer__icon" viewBox="0 0 24 24" aria-hidden="true"><g fill="none" stroke="var(--ink)" stroke-width="2.2" stroke-linecap="round"><path d="M2 9a14 14 0 0 1 20 0"/><path d="M5.5 12.5a9 9 0 0 1 13 0"/><path d="M9 16a4 4 0 0 1 6 0"/></g><circle cx="12" cy="19.5" r="1.8" fill="var(--ink)"/></svg>
        Home Phone Services
      </li>
    </ul>
  </div>

  <div class="location">
    <svg class="location__pin" viewBox="0 0 22 36" aria-hidden="true"><path d="M11 1a10 10 0 0 0-10 10c0 7 10 19 10 19s10-12 10-19A10 10 0 0 0 11 1z" fill="var(--brand-blue)"/><circle cx="11" cy="11" r="3.5" fill="#fff"/><ellipse cx="11" cy="33" rx="6" ry="2" fill="var(--brand-blue)" opacity="0.6"/></svg>
    <span>West Point, NE</span>
  </div>

  <div class="photo photo--mother" role="img" aria-label="Photo of a smiling mother on the phone holding her baby beside a laptop on a table"></div>
</section>

<section class="banner banner--family">
  <div class="brand"><span class="brand__dot"></span><span class="brand__name">NORTHLINK</span></div>
  <p class="tagline">FIBER OPTIC FAST</p>

  <div class="offer">
    <svg class="offer__shape" viewBox="0 0 430 175" preserveAspectRatio="none" aria-hidden="true">
      <polygon points="8,42 384,20 354,156 22,156" fill="var(--accent-green)"/>
      <polygon points="44,20 390,40 378,132 32,166" fill="none" stroke="var(--ink)" stroke-width="4"/>
    </svg>
    <ul class="offer__list">
      <li class="offer__item">
        <svg class="offer__icon" viewBox="0 0 24 24" aria-hidden="true"><path fill="var(--ink)" d="M6.6 10.8a15.1 15.1 0 0 0 6.6 6.6l2.2-2.2a1 1 0 0 1 1-.25 11.4 11.4 0 0 0 3.6.57 1 1 0 0 1 1 1V20a1 1 0 0 1-1 1A17 17 0 0 1 3 4a1 1 0 0 1 1-1h3.5a1 1 0 0 1 1 1c0 1.25.2 2.45.57 3.57a1 1 0 0 1-.25 1z"/><path d="M14 3a7 7 0 0 1 7 7M14 6.5a3.5 3.5 0 0 1 3.5 3.5" fill="none" stroke="var(--ink)" stroke-width="1.8" stroke-linecap="round"/></svg>
        High Speed Internet
      </li>
      <li class="offer__item">
        <svg class="offer__icon" viewBox="0 0 24 24" aria-hidden="true"><g fill="none" stroke="var(--ink)" stroke-width="2.2" stroke-linecap="round"><path d="M2 9a14 14 0 0 1 20 0"/><path d="M5.5 12.5a9 9 0 0 1 13 0"/><path d="M9 16a4 4 0 0 1 6 0"/></g><circle cx="12" cy="19.5" r="1.8" fill="var(--ink)"/></svg>
        Home Phone Services
      </li>
    </ul>
  </div>

  <div class="location">
    <svg class="location__pin" viewBox="0 0 22 36" aria-hidden="true"><path d="M11 1a10 10 0 0 0-10 10c0 7 10 19 10 19s10-12 10-19A10 10 0 0 0 11 1z" fill="var(--brand-blue)"/><circle cx="11" cy="11" r="3.5" fill="#fff"/><ellipse cx="11" cy="33" rx="6" ry="2" fill="var(--brand-blue)" opacity="0.6"/></svg>
    <span>West Point, NE</span>
  </div>

  <div class="photo photo--family" role="img" aria-label="Photo of a multi-generation family on a couch using laptops and tablets together"></div>
</section>

</body>
</html>
```